Keepers of the Halvering Sound CD

We need a CD cover designed that fits the specifications for discavella K-7400 (https://discavell-press.example/templates/pdf/K7400.pdf) We also need the art for the actual CD. We want to emphasize the performers on the CD and "The Keepers of the Halvering Sound." I am uploading the front cover photo, the inside two pages photo background, the back photo. The boat photo is the front, the smoke is the back, and the water is for both middle pages. See attached copy for details

Target Market(s)

People will be buying the CD because it has some great performers and to support a cause.

Colors

Designer to choose colors to be used in the design.

Requirements
Must have
• Visual appeal and it must fit the discavella K-7400 template

```html
<!DOCTYPE html>
<html lang="en">
<head>
<meta charset="utf-8">
<title>Keepers of the Halvering Sound – Back Cover Track List</title>
<link href="https://fonts.googleapis.com/css2?family=EB+Garamond:ital,wght@0,400;0,600;1,400;1,500&display=swap" rel="stylesheet">
<style>
  :root {
    --sky-blue: #8a9cb3;
    --sky-deep: #6f8199;
    --smoke-light: #f2f2f0;
    --smoke-mid: #c9ccd0;
    --smoke-grey: #9fa3a8;
    --ink: #141414;
  }
  html, body {
    margin: 0;
    padding: 0;
    overflow: hidden;
    background: #ffffff;
  }
  .back-cover {
    position: relative;
    width: 1200px;
    height: 914px;
    overflow: hidden;
  }
  .smoke-photo {
    position: absolute;
    inset: 0;
    background:
      radial-gradient(ellipse 420px 320px at 30% 35%, rgba(242,242,240,0.95), rgba(242,242,240,0) 70%),
      radial-gradient(ellipse 380px 300px at 70% 20%, rgba(236,237,238,0.9), rgba(236,237,238,0) 70%),
      radial-gradient(ellipse 360px 420px at 75% 60%, rgba(225,227,230,0.9), rgba(225,227,230,0) 72%),
      radial-gradient(ellipse 500px 260px at 40% 80%, rgba(210,212,215,0.9), rgba(210,212,215,0) 70%),
      radial-gradient(ellipse 300px 260px at 95% 85%, rgba(190,193,198,0.8), rgba(190,193,198,0) 70%),
      linear-gradient(160deg, var(--sky-blue) 0%, var(--smoke-mid) 40%, var(--smoke-grey) 70%, var(--sky-deep) 100%);
  }
  .track-list {
    position: absolute;
    left: 84px;
    top: 64px;
    margin: 0;
    padding: 0;
    list-style: none;
    font-family: "EB Garamond", Garamond, serif;
    font-size: 48px;
    line-height: 58.8px;
    color: var(--ink);
    letter-spacing: -0.3px;
  }
  .track {
    white-space: nowrap;
  }
  .track-number,
  .track-title {
    font-style: italic;
    font-weight: 500;
  }
  .performer {
    font-weight: 600;
  }
</style>
</head>
<body>
<main class="back-cover">
  <div class="smoke-photo" role="img" aria-label="Photograph of white industrial smoke billowing from a smokestack against a blue-grey sky"></div>
  <ol class="track-list">
    <li class="track"><span class="track-number">1.</span> <span class="performer">Corwin Ashdale,</span> <span class="track-title">Salt and Stone: 4:19</span></li>
    <li class="track"><span class="track-number">2.</span> <span class="performer">Maren Holloway,</span> <span class="track-title">Grey Harbour 3:07</span></li>
    <li class="track"><span class="track-number">3.</span> <span class="performer">Ewan Thackery,</span> <span class="track-title">River Road 3:54</span></li>
    <li class="track"><span class="track-number">4.</span> <span class="performer">Rory Lindqvist,</span> <span class="track-title">Iron Shore Blues 5:02</span></li>
    <li class="track"><span class="track-number">5.</span> <span class="performer">The Saltmarsh Reelers,</span> <span class="track-title">Evergreen Reel 3:26</span></li>
    <li class="track"><span class="track-number">6.</span> <span class="performer">Tessa Brightwood,</span> <span class="track-title">Lantern Town 5:33</span></li>
    <li class="track"><span class="track-number">7.</span> <span class="performer">Counting the Tides,</span> <span class="track-title">One Tide from Home 5:09</span></li>
    <li class="track"><span class="track-number">8.</span> <span class="performer">Iona MacKeever,</span> <span class="track-title">Song of the Last Grey Schooner 4:44</span></li>
    <li class="track"><span class="track-number">9.</span> <span class="performer">Callum Durant,</span> <span class="track-title">Neighbours Like You 3:14</span></li>
    <li class="track"><span class="track-number">10.</span> <span class="performer">Elias Paqtnek,</span> <span class="track-title">The Shoreline’s Warning 4:21</span></li>
    <li class="track"><span class="track-number">11.</span> <span class="performer">Owen Harrower,</span> <span class="track-title">Sing it Clearer 4:03</span></li>
    <li class="track"><span class="track-number">12.</span> <span class="performer">Shona MacAlister,</span> <span class="track-title">Out of Reach 4:35</span></li>
    <li class="track"><span class="track-number">13.</span> <span class="performer">Niall Brennick,</span> <span class="track-title">Halvering Landing 3:49</span></li>
    <li class="track"><span class="track-number">14.</span> <span class="performer">Ada Wenlock et al,</span> <span class="track-title">My Own Shoreline 5:12</span></li>
  </ol>
</main>
</body>
</html>
```